Flyer-Design für psychologische Beratungspraxis für Mütter
Zielgruppe
Gelassenheitswerkstatt ist eine psychologische Beratungspraxis. Ich unterstütze Mütter, Schwangere und Frauen mit Kinderwunsch bei Herausforderungen rund um Schwangerschaft, Geburt, Mutterschaft, und damit einhergehenden Problemen.
Aufgabenstellung
Text nochmal geringgradig geändert...siehe Datei anbei

```html
<!DOCTYPE html>
<html lang="de">
<head>
<meta charset="utf-8">
<title>Gelassenheitswerkstatt – Flyer</title>
<link rel="stylesheet" href="https://fonts.googleapis.com/css2?family=Archivo:wght@400;600;800&family=Amatic+SC:wght@700&display=swap">
<style>
  :root {
    --backdrop: #e3e2de;
    --navy: #28307c;
    --navy-soft: #4a52a0;
    --page-left: #e7e9e6;
    --page-right: #f7f7f5;
    --pill: #e3e5ec;
    --highlight: #b8cae6;
    --cover-light: #d9d2c9;
    --cover-warm: #b8742f;
    --cover-dark: #5a3520;
    --photo-cool: #6f77c4;
    --photo-skin: #c99b86;
  }
  * { box-sizing: border-box; margin: 0; padding: 0; }
  html, body { width: 1200px; height: 864px; overflow: hidden; }
  body {
    background: var(--backdrop);
    font-family: "Archivo", Arial, sans-serif;
    color: var(--navy);
    position: relative;
  }
  .page {
    position: absolute;
    top: 252px;
    width: 360px;
    height: 360px;
    overflow: hidden;
  }
  .page--intro { left: 40px; background: var(--page-left); }
  .page--situations { left: 400px; background: var(--page-right); box-shadow: -1px 0 0 rgba(0,0,0,.06); }
  .page--cover { left: 800px; }

  .page-art { position: absolute; inset: 0; }

  .body-copy {
    position: absolute;
    font-size: 7.6px;
    line-height: 1.38;
    color: var(--navy-soft);
  }
  .body-copy p { margin-bottom: 5px; }
  .body-copy strong { color: var(--navy); font-weight: 800; }
  .mark {
    background: var(--highlight);
    border-radius: 6px;
    padding: 0 4px;
    color: var(--navy);
    font-weight: 600;
  }
  .page--intro .body-copy { left: 24px; top: 176px; width: 312px; }

  .section-title {
    position: absolute;
    left: 22px;
    top: 26px;
    background: var(--pill);
    border-radius: 14px;
    padding: 4px 14px 4px 10px;
    font-weight: 800;
    font-size: 19px;
    letter-spacing: .04em;
    color: var(--navy);
  }
  .page--situations .body-copy { left: 26px; top: 66px; width: 312px; }
  .situation-list { list-style: none; margin-bottom: 6px; }
  .situation-list li { padding-left: 9px; text-indent: -9px; }

  .cover-photo { position: absolute; inset: 0; }
  .cover-title {
    position: absolute;
    right: 20px;
    top: 26px;
    display: flex;
    flex-direction: column;
    align-items: flex-end;
    gap: 4px;
    font-family: "Amatic SC", "Comic Sans MS", cursive;
    font-weight: 700;
    font-size: 21px;
    line-height: 1;
    color: var(--navy);
  }
  .cover-title span {
    background: rgba(236,236,240,.92);
    border-radius: 12px;
    padding: 3px 10px 2px;
    letter-spacing: .03em;
  }
  .brand {
    position: absolute;
    right: 40px;
    bottom: 24px;
    display: flex;
    align-items: center;
    gap: 6px;
    font-size: 9px;
    font-weight: 600;
    color: #f3ece4;
    letter-spacing: .05em;
  }
  .brand-dot {
    width: 10px; height: 10px;
    border-radius: 50%;
    border: 1.5px solid #f3ece4;
  }
</style>
</head>
<body>

<section class="page page--intro">
  <svg class="page-art" width="360" height="360" viewBox="0 0 360 360">
    <path d="M248 20 C232 70 260 150 330 150" fill="none" stroke="var(--navy)" stroke-width="1.6"/>
    <circle cx="272" cy="92" r="60" fill="var(--photo-cool)" role="img" aria-label="Foto: Mutter kuschelt mit ihrem neugeborenen Baby"/>
    <circle cx="296" cy="104" r="32" fill="var(--photo-skin)" opacity=".55"/>
  </svg>
  <div class="body-copy">
    <p><strong>Mutter sein ist wunderbar.</strong> Wenn eine Frau Mutter wird, ist sie plötzlich verliebt über beide Ohren, unbändig stolz und von Glücksgefühlen völlig überwältigt. <strong>So ist es doch NORMAL, oder...?</strong></p>
    <p><strong>Überforderung, Frustration</strong> und <strong>Verzweiflung</strong> kennen Mütter, Frauen mit Kinderwunsch und werdende Mütter allerdings ebenfalls nur zu gut. Wichtig ist, dass die Beurteilung einer Situation, d.h. wie stark sie uns belastet, alleine uns selbst zusteht. Nur unsere eigene <strong>subjektive Einschätzung</strong> ist ausschlaggebend.</p>
    <p>So unterschiedlich wir Menschen sind, so verschieden ist auch unser persönliches Fühlen und Erleben. Deshalb benötigen wir <strong>individuell passende Lösungen</strong> für unsere Herausforderungen.</p>
    <p>Ja, Mutter sein ist wundervoll! Und ja, die Dynamik der Paarbeziehung verändert sich schlagartig und wir stehen plötzlich vor einer der erfüllendsten Aufgaben und zugleich einer der größten <strong>existentiellen Herausforderungen</strong>, die uns das Leben bietet: <span class="mark">Eltern sein.</span></p>
  </div>
</section>

<section class="page page--situations">
  <svg class="page-art" width="360" height="360" viewBox="0 0 360 360">
    <path d="M290 360 C292 320 318 296 360 298" fill="none" stroke="var(--navy)" stroke-width="1.6"/>
    <path d="M0 8 C10 4 18 2 24 0" fill="none" stroke="var(--navy)" stroke-width="1.6"/>
    <circle cx="318" cy="344" r="42" fill="#e9dcd4" role="img" aria-label="Foto: kleine Babyhand hält einen Finger"/>
  </svg>
  <h2 class="section-title">WENN ALSO...</h2>
  <div class="body-copy">
    <ul class="situation-list">
      <li>... wir <strong>gern Mutter wären</strong> aber das Leben andere Pläne hat?</li>
      <li>... uns die Erfahrung der <strong>Geburt belastet</strong>, aber niemand zuhört, weil ja „jetzt alles ok ist“?</li>
      <li>... wenn wir unser <strong>Kind verloren</strong> haben?</li>
      <li>... unser Kind oder wir selbst mit einer <strong>Krankheit</strong> zu kämpfen haben?</li>
      <li>... wir selbst oder unser Partner uns <strong>kaum wiedererkennen?</strong></li>
      <li>... wenn wir uns treu bleiben wollen, aber uns dennoch durch die Meinung anderer <strong>verunsichern</strong> lassen?</li>
      <li>... wir eben <strong>nicht stolz</strong> darauf sind, wie wir den letzten Schreianfall unseres Babys begleitet haben?</li>
      <li>... wir weder die Wut unseres Kindes, noch unsere eigene <strong>Wut</strong> gebändigt bekommen?</li>
      <li>... wir mit der Situation <strong>überfordert</strong> sind und nicht mehr weiter wissen?</li>
    </ul>
    <p>Um trotz Rückschlägen ein zufriedenes Leben zu führen und um feinfühlig für unsere Kinder da zu sein, benötigen wir viel Kraft. Mentale Kraft, die es uns ermöglicht, aus den Augen unserer Kinder zu sehen, unsere eigenen Gefühle zu regulieren und die starken Gefühle unserer Kinder auszuhalten und zu begleiten.</p>
    <p>Gemeinsam erarbeiten wir <span class="mark">individuelle Strategien,</span> wie Sie auf Ihre eigenen Ressourcen besser zugreifen, und so mental gestärkt nach vorne schauen können.</p>
  </div>
</section>

<section class="page page--cover">
  <svg class="cover-photo" width="360" height="360" viewBox="0 0 360 360" role="img" aria-label="Foto: Mutter hält ihr Kind im Arm, im warmen Gegenlicht eines Feldes">
    <defs>
      <linearGradient id="cover-tone" x1="0" y1="0" x2="0" y2="1">
        <stop offset="0" stop-color="var(--cover-light)"/>
        <stop offset=".35" stop-color="#9b7a5c"/>
        <stop offset=".6" stop-color="var(--cover-warm)"/>
        <stop offset="1" stop-color="var(--cover-dark)"/>
      </linearGradient>
    </defs>
    <rect width="360" height="360" fill="url(#cover-tone)"/>
  </svg>
  <h1 class="cover-title">
    <span>Krisenbegleitung und Lebensberatung</span>
    <span>für Mütter, Schwangere</span>
    <span>und Frauen mit Kinderwunsch</span>
  </h1>
  <div class="brand"><span class="brand-dot"></span>Gelassenheitswerkstatt</div>
</section>

</body>
</html>
```